Email signature design - law firm

We are a small boutique law firm which is located near the beach in Manly, Australia.

We have just recently developed a new logo and are looking to redesign our letterhead, business cards and email signatures.

This brief is for our email signatures. This is an email signature to appear at the bottom of our Outlook emails so we would like it to be text that we are able to edit as the wording in our email signature often required amendments.

I have attached a word document which had our new logo, and our previous email signature which all the information/wording that needs to be included.

We would like multiple designs with a modern, simplistic yet striking look.

Thanks.

font - raleway or montserrat

Need extra days to review

• Must have the exact wording which appears in the email signature in the word document attached to brief.
• Must be able to edit the text as it is for an Outlook email signature which wording will change from time to time.

```html
<!DOCTYPE html>
<html lang="en">
<head>
<meta charset="utf-8">
<title>Harlow &amp; Partners – Letterhead and Email Signature</title>
<link href="https://fonts.googleapis.com/css2?family=Lato:wght@400;700&family=Montserrat:wght@600&display=swap" rel="stylesheet">
<style>
  :root {
    --backdrop: #2b2b2b;
    --paper: #ffffff;
    --navy: #2f3b8a;
    --band: #34408c;
    --gold: #a88a4c;
    --ink: #333333;
    --faint: #e9e9e9;
  }
  * { margin: 0; padding: 0; box-sizing: border-box; }
  html, body { width: 800px; height: 1200px; overflow: hidden; }
  body {
    position: relative;
    background: var(--backdrop);
    font-family: "Lato", sans-serif;
    color: var(--ink);
  }

  /* Letterhead */
  .letterhead {
    position: absolute;
    left: 146px; top: 61px;
    width: 509px; height: 761px;
    background: var(--paper);
    overflow: hidden;
  }
  .brand {
    position: absolute;
    text-align: center;
    font-family: "Montserrat", sans-serif;
    font-weight: 600;
    color: var(--navy);
  }
  .brand-mark {
    display: block;
    margin: 0 auto 6px;
    width: 14px; height: 14px;
    border-radius: 50%;
    background: var(--navy);
  }
  .brand-name { display: block; font-size: 12px; letter-spacing: 0.5px; white-space: nowrap; }
  .brand-sub { display: block; font-size: 5.5px; letter-spacing: 4px; margin-top: 3px; }
  .letterhead .brand { left: 0; right: 0; top: 28px; }

  .letterhead-watermark {
    position: absolute;
    left: 200px; top: 330px;
    width: 110px; height: 110px;
    border-radius: 50%;
    background: var(--faint);
  }

  .letterhead-contact {
    position: absolute;
    right: 84px; top: 713px;
    font-size: 11px;
    white-space: nowrap;
  }
  .label { color: var(--navy); }
  .web { color: var(--navy); }
  .web .domain { color: var(--gold); }

  .letterhead-band {
    position: absolute;
    left: 0; top: 733px;
    width: 100%; height: 28px;
    background: var(--band);
    color: #fff;
    font-size: 11px;
    line-height: 28px;
    padding-left: 84px;
    white-space: nowrap;
  }
  .corner-dot {
    position: absolute;
    width: 44px; height: 44px;
    border-radius: 50%;
    background: var(--navy);
    border: 5px solid #fff;
  }
  .letterhead .corner-dot { right: 6px; top: 706px; }

  /* Email signature */
  .signature {
    position: absolute;
    left: 146px; top: 856px;
    width: 509px; height: 286px;
    background: var(--paper);
    overflow: hidden;
  }
  .signature-details {
    position: absolute;
    left: 38px; top: 24px;
  }
  .sign-off { font-size: 11.5px; line-height: 14px; }
  .signer { font-size: 14.5px; font-weight: 700; color: var(--navy); line-height: 18px; margin-bottom: 6px; }
  .sig-line { font-size: 11.5px; line-height: 14px; }
  .sig-firm { font-size: 11.5px; color: var(--navy); font-weight: 700; margin-top: 6px; line-height: 15px; }
  .sig-address { font-size: 11.5px; color: #555; line-height: 14px; }
  .signature .brand { left: 338px; width: 160px; top: 32px; }
  .signature .brand-name { font-size: 9.5px; }
  .signature .brand-sub { font-size: 5px; }

  .disclaimer {
    position: absolute;
    left: 0; top: 132px;
    width: 100%; height: 154px;
    background: var(--band);
    color: #fff;
    font-size: 7px;
    line-height: 8.8px;
    padding: 15px 60px 0 37px;
  }
  .disclaimer p + p { margin-top: 9px; }
  .signature .corner-dot { right: 4px; top: 114px; }
</style>
</head>
<body>

<section class="letterhead">
  <div class="brand">
    <span class="brand-mark"></span>
    <span class="brand-name">Harlow &amp; Partners</span>
    <span class="brand-sub">LAWYERS</span>
  </div>
  <div class="letterhead-watermark"></div>
  <p class="letterhead-contact">
    <span class="label">P:</span> (02) 5550 1482 | <span class="label">F:</span> (02) 5550 1483 |
    <span class="web">www.<span class="domain">harlowandpartners</span>.com.au</span>
  </p>
  <div class="letterhead-band">HARLOW &amp; PARTNERS:&nbsp; Suite 4, 12 Ocean Lane, SEACLIFF&nbsp;&nbsp;&nbsp; NSW&nbsp;&nbsp; 2099</div>
  <span class="corner-dot"></span>
</section>

<section class="signature">
  <div class="signature-details">
    <p class="sign-off">Regards</p>
    <p class="signer">Megan Doyle</p>
    <p class="sig-line"><span class="label">P:</span> (02) 5550 1482 | <span class="label">F:</span> (02) 5550 1483</p>
    <p class="sig-line web">www.<span class="domain">harlowandpartners</span>.com.au</p>
    <p class="sig-firm">Harlow &amp; Partners</p>
    <p class="sig-address">Suite 4, 12 Ocean Lane, SEACLIFF&nbsp; NSW&nbsp; 2099</p>
  </div>
  <div class="brand">
    <span class="brand-mark"></span>
    <span class="brand-name">Harlow &amp; Partners</span>
    <span class="brand-sub">LAWYERS</span>
  </div>
  <div class="disclaimer">
    <p>Important note: This E-Mail and any attachment is PRIVILEGED and confidential. It must not be read, copied, disclosed or used by any person other than the above named addressees. In order to preserve the intended confidentiality and privilege, please notify us immediately if you have received this e-mail by mistake and secure-delete this e-mail from your system.<br>Unauthorised perusal, use, disclosure, forwarding or copying is strictly prohibited and may be unlawful.</p>
    <p>Liability limited by a scheme approved under Professional Standards Legislation. Legal practitioners at CoastLaw (NSW) Pty Ltd are members of the scheme.</p>
    <p>Fraud warning: Please be aware that there is a significant risk posed by cyber fraud, specifically relating to email accounts and bank account details. Our bank account details will never change during the course of a transaction, and we will never advise you of a change to our bank details via email. Please check account details with us in person or by phone before making payments. If you advise us of your bank account details by email, please also ring and confirm the bank account details by phone as well.</p>
  </div>
  <span class="corner-dot"></span>
</section>

</body>
</html>
```